Business Card Design - cloud video monitoring

For the trade show in Las Vegas our company needs business cards with new brand - Vantrolux

The logo of the new brand is attached, the sample card with the founder's contact details is attached (just change the website to www.vantrolux.me) and email to info@vantrolux.me
Updates

                                        Forgot to say: the tagline for the brand is "the new normal cloud video management"

Industry/Entity Type

Business

```html
<!DOCTYPE html>
<html lang="en">
<head>
<meta charset="utf-8">
<title>Vantrolux Business Card</title>
<link rel="stylesheet" href="https://fonts.googleapis.com/css2?family=Electrolize&display=swap">
<style>
  :root {
    --card-dark: #2b3339;
    --brand-green: #4ff58f;
    --panel-white: #f3f4f4;
    --divider: #3a4046;
    --text-dark: #262c31;
    --text-light: #e9eef0;
    --text-muted: #aeb8bd;
    --stage: #d9dadb;
  }
  * { margin: 0; padding: 0; box-sizing: border-box; }
  html, body { width: 1200px; height: 949px; overflow: hidden; }
  body {
    background: radial-gradient(ellipse at 45% 40%, #f1f1f1 0%, var(--stage) 75%);
    font-family: "Electrolize", "Trebuchet MS", sans-serif;
    position: relative;
  }
  .card {
    position: absolute;
    top: 177px;
    width: 340px;
    height: 595px;
    background: var(--card-dark);
    border-radius: 22px;
    overflow: hidden;
    box-shadow: 0 18px 40px rgba(0,0,0,0.22);
  }
  .card--back { left: 230px; }
  .card--front { left: 630px; }

  .brand {
    display: flex;
    align-items: center;
    gap: 14px;
    color: var(--brand-green);
    letter-spacing: 1px;
  }
  .brand__dot {
    border: 5px solid var(--brand-green);
    border-radius: 50%;
    flex: none;
  }
  .tagline {
    color: var(--text-muted);
    letter-spacing: 0.6px;
    white-space: nowrap;
  }

  /* back side */
  .back-lockup {
    position: absolute;
    top: 258px;
    left: 0; right: 0;
    display: flex;
    flex-direction: column;
    align-items: center;
    gap: 14px;
  }
  .card--back .brand { font-size: 40px; }
  .card--back .brand__dot { width: 52px; height: 52px; }
  .card--back .tagline { font-size: 13px; }
  .social {
    position: absolute;
    right: 24px;
    bottom: 30px;
    display: flex;
    gap: 14px;
  }
  .social__mark {
    width: 14px; height: 14px;
    border-radius: 50%;
    background: var(--text-light);
  }
  .back-band {
    position: absolute;
    left: 0; right: 0; bottom: 0;
    height: 12px;
    background: var(--brand-green);
  }

  /* front side */
  .card-header {
    position: absolute;
    top: 0; left: 0; right: 0;
    height: 205px;
    padding: 40px 30px 0;
  }
  .card--front .brand { font-size: 32px; }
  .card--front .brand__dot { width: 44px; height: 44px; }
  .card--front .tagline {
    margin-top: 10px;
    font-size: 11.5px;
  }
  .holder {
    margin-top: 30px;
    display: flex;
    align-items: center;
    gap: 10px;
    color: var(--text-light);
    font-size: 17px;
    letter-spacing: 2px;
  }
  .holder__role { margin-left: 22px; letter-spacing: 1.5px; }
  .holder svg { width: 16px; height: 16px; fill: var(--brand-green); }

  .contact-panel {
    position: absolute;
    top: 205px;
    left: 0;
    width: 318px;
    bottom: 22px;
    background: var(--panel-white);
    border-bottom-right-radius: 4px;
  }
  .contact-panel::before {
    content: "";
    position: absolute;
    left: 0; top: 0; bottom: 20px;
    width: 16px;
    background: var(--brand-green);
  }
  .contact-list { list-style: none; }
  .contact-item {
    height: 92px;
    display: flex;
    align-items: center;
    gap: 18px;
    padding-left: 38px;
    border-bottom: 1.5px solid var(--divider);
    color: var(--text-dark);
    font-size: 19px;
    letter-spacing: 0.8px;
    line-height: 1.3;
  }
  .contact-item:last-child { border-bottom: none; }
  .contact-item svg { width: 24px; height: 24px; flex: none; fill: var(--brand-green); }
  .contact-item--small { font-size: 16px; }
</style>
</head>
<body>

  <section class="card card--back" aria-label="Card back">
    <div class="back-lockup">
      <div class="brand">
        <span class="brand__dot"></span>
        <span class="brand__name">Vantrolux</span>
      </div>
      <p class="tagline">the new normal cloud video management</p>
    </div>
    <div class="social" aria-label="Social links">
      <span class="social__mark"></span>
      <span class="social__mark"></span>
      <span class="social__mark"></span>
    </div>
    <div class="back-band"></div>
  </section>

  <section class="card card--front" aria-label="Card front">
    <header class="card-header">
      <div class="brand">
        <span class="brand__dot"></span>
        <span class="brand__name">Vantrolux</span>
      </div>
      <p class="tagline">the new normal cloud video management</p>
      <div class="holder">
        <svg viewBox="0 0 16 16"><circle cx="8" cy="4.5" r="3.5"/><path d="M1 16c0-4 3-6.5 7-6.5s7 2.5 7 6.5z"/></svg>
        <span class="holder__name">MAREK ONDRA</span>
        <span class="holder__role">founder</span>
      </div>
    </header>

    <div class="contact-panel">
      <ul class="contact-list">
        <li class="contact-item">
          <svg viewBox="0 0 24 24"><path d="M6.6 10.8a15.1 15.1 0 0 0 6.6 6.6l2.2-2.2a1 1 0 0 1 1-.25 11.4 11.4 0 0 0 3.6.57 1 1 0 0 1 1 1V20a1 1 0 0 1-1 1A17 17 0 0 1 3 4a1 1 0 0 1 1-1h3.5a1 1 0 0 1 1 1c0 1.25.2 2.45.57 3.57a1 1 0 0 1-.25 1z"/></svg>
          <span>012 555 0142</span>
        </li>
        <li class="contact-item">
          <svg viewBox="0 0 24 24"><path d="M2 5h20v14H2z M3.5 6.5 12 13l8.5-6.5" stroke="#f3f4f4" stroke-width="1.4"/></svg>
          <span>info@vantrolux.me</span>
        </li>
        <li class="contact-item">
          <svg viewBox="0 0 24 24"><circle cx="12" cy="12" r="10"/><path d="M2 12h20M12 2c-3.5 3.5-3.5 16.5 0 20M12 2c3.5 3.5 3.5 16.5 0 20M4 7h16M4 17h16" stroke="#f3f4f4" stroke-width="1.2" fill="none"/></svg>
          <span class="contact-item--small">www.vantrolux.me</span>
        </li>
        <li class="contact-item">
          <svg viewBox="0 0 24 24"><path d="M12 2a7 7 0 0 0-7 7c0 5.2 7 13 7 13s7-7.8 7-13a7 7 0 0 0-7-7zm0 9.5A2.5 2.5 0 1 1 12 6.5a2.5 2.5 0 0 1 0 5z"/></svg>
          <span>204,9th floor,Crest<br>Harbor Avenue NRV</span>
        </li>
      </ul>
    </div>
  </section>

</body>
</html>
```